Business Card Design Project

We have a logo design and are now looking for a business card design. We supply pre-construction services to the Wireless Telecommunication Industry in the development of cell phone tower and other antenna supporting infrastructure e.g. buildings. The types of services include Real Estate Leasing, Zoning & Permitting,Surveying and A&E work. I am looking for a card that includes the logo we have selected along with the full company name. Company colors are Blue and Silver. I want something professional and that "pops". Use your imagination with the four sided star portion of the logo - it can be stretched such that it occupies a large portion of the card or kept simple the way it is. I am interested in seeing the design on a white, silver, navy, black or charcoal background or any other color you think works well with the logo. Apart from the logo that includes LNI we also need to see the full company name on the card - Lanternway Networks, Inc. The design must also show a persons name, title, address, (2) phone numbers, e-mail address and web address www.lni-sample.co

Target Market(s)

Cell phone carriers e.g. Coravent Mobile, QB&R, K-Cellix, Dunmo etc.

Industry/Entity Type

Cell Phone

Requirements
Must have
• Logo and
Lanternway Networks, Inc.

```html
<!DOCTYPE html>
<html lang="en">
<head>
<meta charset="utf-8">
<title>Lanternway Networks, Inc. – Business Card</title>
<link rel="stylesheet" href="https://fonts.googleapis.com/css2?family=Anton&family=Open+Sans:wght@400;600;700&display=swap">
<style>
  :root {
    --page: #e9e9ec;
    --card-white: #ffffff;
    --brand-blue: #1a6fd0;
    --text-blue: #2a8fd6;
    --silver-light: #f4f4f4;
    --silver-mid: #c9c9cb;
    --silver-dark: #a9a9ac;
    --label-white: #ffffff;
  }
  * { box-sizing: border-box; margin: 0; padding: 0; }
  html, body { width: 1200px; height: 1000px; overflow: hidden; }
  body {
    background: var(--page);
    font-family: "Open Sans", Arial, sans-serif;
    position: relative;
  }
  .card {
    position: absolute;
    left: 210px;
    width: 780px;
    height: 446px;
    border-radius: 30px;
    overflow: hidden;
    background: var(--card-white);
    box-shadow: 0 6px 22px rgba(0,0,0,0.18);
  }
  .card--front { top: 36px; }
  .card--back { top: 518px; }

  /* Front */
  .front-decoration {
    position: absolute; inset: 0;
    background: radial-gradient(ellipse 62% 58% at 50% 50%, var(--card-white) 0%, var(--card-white) 55%, var(--silver-light) 72%, var(--silver-mid) 100%);
  }
  .front-brand {
    position: absolute;
    left: 50%; top: 50%;
    transform: translate(-50%, -50%);
    display: flex; align-items: center; gap: 24px;
  }
  .front-brand__dot {
    width: 56px; height: 56px; border-radius: 50%;
    background: var(--brand-blue);
  }
  .front-brand__name {
    font-family: "Anton", Impact, sans-serif;
    font-size: 120px; line-height: 1;
    color: var(--brand-blue);
    letter-spacing: 4px;
  }

  /* Back */
  .back-company {
    position: absolute;
    left: 46px; top: 52px;
    font-family: "Anton", Impact, sans-serif;
    font-weight: 400;
    font-size: 58px; line-height: 1;
    color: var(--brand-blue);
    letter-spacing: 0.5px;
    white-space: nowrap;
  }
  .back-rule {
    position: absolute; left: 0; right: 0; top: 166px;
    height: 12px; background: var(--brand-blue);
  }
  .back-panel {
    position: absolute; left: 0; right: 0; top: 178px; bottom: 0;
    background: radial-gradient(ellipse 45% 70% at 52% 48%, var(--silver-light) 0%, var(--silver-mid) 70%, var(--silver-dark) 100%);
  }
  .address {
    position: absolute; left: 42px; top: 32px;
    color: var(--text-blue); font-size: 18px; line-height: 30px;
  }
  .address__label { color: var(--label-white); font-size: 20px; }
  .address__line { letter-spacing: 2px; }
  .web {
    position: absolute; left: 36px; bottom: 26px;
    display: flex; align-items: center; gap: 12px;
    color: var(--text-blue); font-size: 20px;
  }
  .person {
    position: absolute; right: 44px; top: 34px;
    text-align: right;
  }
  .person__name { color: var(--label-white); font-weight: 700; font-size: 24px; line-height: 32px; }
  .person__title { color: var(--text-blue); font-size: 26px; line-height: 36px; }
  .contacts {
    position: absolute; right: 40px; bottom: 18px;
    text-align: right; color: var(--text-blue); font-size: 20px; line-height: 32px;
  }
  .contacts__row { display: flex; justify-content: flex-end; align-items: center; gap: 10px; }
  .icon { width: 16px; height: 16px; flex: none; }
</style>
</head>
<body>

<section class="card card--front" aria-label="Card front">
  <div class="front-decoration" role="img" aria-label="Silver stretched-star decoration radiating from the card corners"></div>
  <div class="front-brand">
    <span class="front-brand__dot"></span>
    <span class="front-brand__name">LNI</span>
  </div>
</section>

<section class="card card--back" aria-label="Card back">
  <h1 class="back-company">Lanternway Networks, Inc.</h1>
  <div class="back-rule"></div>
  <div class="back-panel">
    <div class="address">
      <div class="address__label">Address</div>
      <div class="address__line">**********</div>
      <div class="address__line">**********</div>
      <div class="address__line">**********</div>
    </div>
    <div class="web">
      <svg class="icon" viewBox="0 0 16 16" aria-hidden="true" fill="none" stroke="#ffffff" stroke-width="1.2">
        <circle cx="8" cy="8" r="7"/><ellipse cx="8" cy="8" rx="3" ry="7"/><path d="M1 8h14M2.5 4.5h11M2.5 11.5h11"/>
      </svg>
      <span>www.lni-sample.co</span>
    </div>
    <div class="person">
      <div class="person__name">persons name</div>
      <div class="person__title">title</div>
    </div>
    <div class="contacts">
      <div class="contacts__row"><span>12345678910</span>
        <svg class="icon" viewBox="0 0 16 16" aria-hidden="true"><path fill="#ffffff" d="M4 1l3 3-2 2c1 2 3 4 5 5l2-2 3 3-2 3C7 15 1 9 1 3z"/></svg>
      </div>
      <div class="contacts__row"><span>12345678910</span>
        <svg class="icon" viewBox="0 0 16 16" aria-hidden="true"><rect x="4" y="1" width="8" height="14" rx="1.5" fill="none" stroke="#ffffff" stroke-width="1.4"/><circle cx="8" cy="12.5" r="0.9" fill="#ffffff"/></svg>
      </div>
      <div class="contacts__row"><span>lni@mailbox-sample.co</span>
        <svg class="icon" viewBox="0 0 16 16" aria-hidden="true" fill="none" stroke="#ffffff" stroke-width="1.3"><rect x="1" y="3" width="14" height="10"/><path d="M1 3l7 6 7-6"/></svg>
      </div>
    </div>
  </div>
</section>

</body>
</html>
```